Manuka honey jar label for new Manuka brand

We are planning to start a Manuka honey brand and we need to design the label for the honey jar. Manuka honey is an up and coming product and the market is still young in our country.
Our market is dominated by 1 brand: Korivo Vital (photo attached). To the people who know what Manuka honey is, they associate it with Korivo Vital in the same way people associate Cola with Zibo Zesta or printer copies with Pluvex.
The good news is that a lot of people do not know yet what Manuka honey is and we still have the opportunity of being the first brand they get to know. At the same time, we still need to be able to take at least a bite out of the Korivo Vital market share.
The Korivo Vital label for their jar I think is not just absolutely gorgeous but it also does its job extremely well. It only features 3 informations:
- name of brand/logo (Korivo Vital)
- name of product (Manuka Honey)
- and mgo rating which is like a rating of how strong the honey is
By having just this information on a relatively small label, their label SCREAMS Manuka by having the Manuka words twice (the brand and the product name) and people develop this association between Korivo Vital and Manuka products in general.
Our product will also be in a similar square plastic jar. It will also be dark tinted, that´s important to note. We can also go for a blue cap but in order to differentiate ourselves from Korivo Vital we thought of maybe choosing a black lid instead. I uploaded 2 jars, 1 with black lid and 1 with gold (although it looks more like mustard) that you can use for simulations. They are pretty accurate of the type of jars and lids that we can have.
The label has total length of about 20cm. One side of the jar has 5,5 cm of the label and the height of the label is 4,5 cm. We can also use selective gold laminating on the label but we cannot have custom shape label at this point as Korivo Vital does with its tree logo that sticks outside the label.
I need the design for the entire label but the focus should be on the front part, that is the part that sells and catches your eye. Like Korivo Vital, the front part I want to have 3 vital informations:
- name of brand/logo (in our case Halvern Terra) - we do not have a pre-existing logo, this needs to be created alongside the label
- and mgo rating
As "other" information we also need the net weight "250 g" alongside with the typical "e" to appear on the front. That is a legal requirement.
Optionally, you can add a small phrase somewhere like "Harvested in New Zealand" or "Made in New Zealand" since this is a product that is only made there and in some areas of Australia.
This is pretty much all the info. As a final note, there are a ton of beautiful premium Manuka honey jar labels. But they are too fancy and when you look at them you don´t instantly recognize that it is Manuka Honey.
This instant recognition is vital! With this small jar there is the danger for customers to think that maybe it´s medicine, maybe it´s sports supplements etc. This is a relatively small product and imagine you just glance on it on the retail shelf. Instantly you must think it is Manuka Honey and that it is beautiful. And if you see it on the shelf next to Korivo Vital, it would be best to also think that you would rather buy this (it gives you more trust) than the Korivo Vital.
One final note: I do not want the bee as an insect on the label. I think some people are turned off when they see an insect with its small legs and make a bad association that there are insects inside. I do not mind symbolism or somehow super stylized bee in a modern way, but I do not want a plain insect on the label.
For any other questions, I am at your disposal. Thank you very much for taking the time to send us a proposal!

```html
<!DOCTYPE html>
<html lang="en">
<head>
<meta charset="utf-8">
<title>Halvern Terra Manuka Honey Label</title>
<link rel="stylesheet" href="https://fonts.googleapis.com/css2?family=Montserrat:wght@600;700&family=Quicksand:wght@500;600&display=swap">
<style>
  :root {
    --page: #ffffff;
    --red-core: #e0141b;
    --red-mid: #c10d13;
    --red-edge: #8f0a0d;
    --gold: #d4a91a;
    --gold-light: #f1d256;
    --gold-dark: #9c7a0c;
    --ink: #0c0c0c;
    --white: #ffffff;
    --bee-yellow: #f3c21c;
  }
  * { margin: 0; padding: 0; box-sizing: border-box; }
  html, body {
    width: 1200px; height: 1000px; overflow: hidden;
    background: var(--page);
  }
  .label {
    position: absolute; left: 110px; top: 91px;
    width: 980px; height: 818px;
    overflow: hidden;
  }
  .label-field {
    position: absolute; inset: 0;
    background: radial-gradient(ellipse at 50% 45%, var(--red-core) 0%, var(--red-mid) 55%, var(--red-edge) 100%);
  }
  .gold-rule {
    position: absolute; left: 0; right: 0; height: 12px;
    background: linear-gradient(180deg, var(--gold-light), var(--gold) 50%, var(--gold-dark));
  }
  .gold-rule.top { top: 8px; }
  .gold-rule.bottom { bottom: 14px; }
  .brand-mark {
    position: absolute; left: 50%; top: 98px;
    width: 130px; height: 130px; margin-left: -65px;
    border-radius: 50%; background: var(--white);
  }
  .brand-name {
    position: absolute; left: 0; right: 0; top: 270px;
    text-align: center; color: var(--white);
    font: 500 60px/1 "Quicksand", sans-serif;
  }
  .product-name {
    position: absolute; left: 70px; top: 400px;
    width: 842px; height: 130px;
    border: 10px solid var(--gold); border-radius: 30px;
    background: var(--ink);
    display: flex; align-items: center; justify-content: center;
    color: var(--gold);
    font: 600 76px/1 "Montserrat", sans-serif;
    letter-spacing: 1px;
  }
  .net-weight {
    position: absolute; left: 170px; top: 618px;
    width: 295px; height: 100px; border-radius: 50px;
    background: var(--ink); color: var(--white);
    display: flex; align-items: center; justify-content: flex-end; padding-right: 34px;
    font: 700 50px/1 "Montserrat", sans-serif;
  }
  .net-weight .estimated { font-weight: 600; font-size: 58px; margin-left: 6px; }
  .mgo-badge { position: absolute; left: 40px; top: 570px; width: 180px; height: 208px; }
  .mgo-badge svg { position: absolute; inset: 0; }
  .mgo-value {
    position: absolute; left: 0; right: 0; top: 52px; text-align: center;
    color: var(--white); font: 700 56px/1 "Montserrat", sans-serif;
  }
  .mgo-unit {
    position: absolute; left: 0; right: 0; top: 116px; text-align: center;
    color: var(--white); font: 700 36px/1 "Montserrat", sans-serif;
  }
  .bee-art {
    position: absolute; left: 765px; top: 515px; width: 160px; height: 150px;
    border-radius: 50% 50% 45% 45%;
    background: radial-gradient(circle at 45% 70%, var(--bee-yellow) 0%, #f7e7b0 45%, rgba(255,255,255,0.9) 70%, rgba(255,255,255,0) 72%);
  }
  .origin {
    position: absolute; left: 590px; top: 640px; width: 360px;
    transform: rotate(-15deg); transform-origin: center;
    color: var(--white); text-align: center;
    font-family: "Quicksand", sans-serif;
  }
  .origin-lead { display: block; font-weight: 500; font-size: 38px; margin-left: -120px; }
  .origin-place { display: block; font-weight: 600; font-size: 56px; line-height: 1; margin-top: 2px; }
</style>
</head>
<body>
  <main class="label">
    <div class="label-field" role="img" aria-label="Deep red label ground with a faint repeating flower pattern"></div>
    <div class="gold-rule top"></div>
    <div class="gold-rule bottom"></div>

    <div class="brand-mark"></div>
    <div class="brand-name">Halvern Terra</div>

    <div class="product-name">Manuka Honey</div>

    <div class="net-weight">250 g<span class="estimated">℮</span></div>

    <div class="mgo-badge">
      <svg viewBox="0 0 180 208" width="180" height="208" aria-hidden="true">
        <polygon points="90,4 176,54 176,154 90,204 4,154 4,54" fill="var(--ink)"/>
        <polygon points="90,16 166,60 166,148 90,192 14,148 14,60" fill="var(--gold)" stroke="var(--gold-light)" stroke-width="4"/>
      </svg>
      <div class="mgo-value">515+</div>
      <div class="mgo-unit">mgo</div>
    </div>

    <div class="bee-art" role="img" aria-label="Small stylised cartoon bee illustration"></div>

    <div class="origin">
      <span class="origin-lead">Harvested in</span>
      <span class="origin-place">New Zealand</span>
    </div>
  </main>
</body>
</html>
```